The Guiding Spark LLC
because everyone deserves a fan
The Guiding Spark LLC -
Creative Brief
Bright & Fun-filled
Rosalind K Delgado
Personal Mentor
2871 S Whitcomb Ave Garden Unit Chicago IL 60619
rdelgado@theguidingspark.example
www.theguidingspark.example
Our Time Together Date: Time: Ask about our Friend Bonus program

```html
<!DOCTYPE html>
<html lang="en">
<head>
<meta charset="utf-8">
<title>The Guiding Spark LLC – Stationery Set</title>
<link href="https://fonts.googleapis.com/css2?family=Open+Sans:wght@400;600;700&display=swap" rel="stylesheet">
<style>
  :root {
    --blue: #1f5fa8;
    --blue-light: #3d8fd8;
    --orange: #f08a1c;
    --green: #7dc242;
    --green-dark: #3e9a3a;
    --dark: #1b1e23;
    --dark-2: #2a2e35;
    --paper: #ffffff;
    --backdrop: #eceef0;
    --ink: #4a4f57;
    --faint: #e3e9f1;
  }
  * { box-sizing: border-box; margin: 0; padding: 0; }
  html, body { width: 1200px; height: 281px; overflow: hidden; }
  body { font-family: "Open Sans", Arial, sans-serif; background: var(--backdrop); position: relative; color: var(--ink); }

  .identity-panel { position: absolute; left: 0; top: 0; width: 366px; height: 281px;
    background: radial-gradient(ellipse at 50% 20%, var(--dark-2), var(--dark)); }

  .brand-lockup { position: absolute; left: 0; width: 366px; top: 14px; text-align: center; }
  .brand-lockup .mark { width: 38px; height: 38px; border-radius: 50%; background: var(--blue-light); margin: 0 auto 5px; }
  .brand-lockup .name { font-weight: 700; font-size: 15px; color: var(--blue-light); line-height: 1; }
  .brand-lockup .tagline { font-size: 6px; color: #9aa3ad; margin-top: 3px; }

  .card { position: absolute; top: 182px; width: 79px; height: 47px; border-radius: 2px; overflow: hidden;
    box-shadow: 0 1px 3px rgba(0,0,0,.5); font-size: 3.4px; line-height: 1.35; }
  .card svg.wave { position: absolute; left: 0; bottom: 0; width: 100%; height: 14px; }
  .card-back { left: 12px; background: var(--paper); padding: 5px 6px; }
  .card-back .title { font-weight: 700; font-size: 4.5px; color: var(--blue); margin-bottom: 3px; }
  .card-back .field { border-bottom: .4px solid #b8c0ca; margin-bottom: 3px; }
  .card-front { left: 100px; background: var(--paper); padding: 5px 6px; }
  .mini-brand { display: flex; align-items: center; gap: 2px; }
  .mini-brand .dot { width: 7px; height: 7px; border-radius: 50%; background: var(--blue-light); }
  .mini-brand span { font-weight: 700; font-size: 4.2px; color: var(--blue); }
  .card-front .person { margin-top: 4px; font-weight: 700; font-size: 4px; color: var(--blue); }
  .card-contact { left: 192px; background: linear-gradient(135deg, #2a78c4, #0f3c74); color: #fff; padding: 6px; }
  .card-contact .person { font-weight: 700; font-size: 4.4px; }
  .card-promo { left: 283px; background: linear-gradient(135deg, #a9db6c, var(--green-dark)); color: #fff; display: flex; flex-direction: column; align-items: center; justify-content: center; }
  .card-promo .dot { width: 12px; height: 12px; border-radius: 50%; background: rgba(255,255,255,.85); margin-bottom: 3px; }
  .card-promo span { font-weight: 700; font-size: 4.6px; }

  .letterhead { position: absolute; top: 12px; width: 136px; height: 247px; background: var(--paper);
    box-shadow: 0 1px 4px rgba(0,0,0,.18); overflow: hidden; }
  .letterhead.first { left: 384px; }
  .letterhead.second { left: 552px; }
  .letterhead .mini-brand { position: absolute; left: 9px; top: 10px; }
  .letterhead .mini-brand .dot { width: 9px; height: 9px; }
  .letterhead .mini-brand span { font-size: 4.6px; }
  .letterhead .address { position: absolute; right: 9px; top: 10px; width: 58px; font-size: 2.6px; line-height: 1.4; text-align: right; }
  .letterhead .backdrop-mark { position: absolute; left: 33px; top: 72px; width: 70px; height: 70px; border-radius: 50%; background: var(--faint); }
  .letterhead .backdrop-name { position: absolute; left: 0; width: 100%; top: 148px; text-align: center; font-weight: 700; font-size: 6px; color: var(--faint); }
  .letterhead svg.wave { position: absolute; left: 0; bottom: 0; width: 136px; height: 26px; }
  .letterhead .footer-web { position: absolute; left: 0; width: 100%; bottom: 4px; text-align: center; font-size: 2.8px; color: #fff; }

  .envelope-front { position: absolute; left: 737px; top: 108px; width: 110px; height: 82px; background: var(--paper);
    box-shadow: 0 1px 4px rgba(0,0,0,.18); overflow: hidden; }
  .envelope-front .mini-brand { position: absolute; left: 6px; top: 6px; }
  .envelope-front .return { position: absolute; left: 6px; top: 16px; font-size: 2.4px; line-height: 1.4; width: 60px; }
  .envelope-front svg.wave { position: absolute; left: 0; bottom: 0; width: 110px; height: 18px; }

  .envelope-back { position: absolute; left: 883px; width: 161px; box-shadow: 0 1px 4px rgba(0,0,0,.2); }
  .envelope-back svg { display: block; width: 100%; height: 100%; }
  .envelope-back.green { top: 100px; height: 52px; }
  .envelope-back.blue { top: 142px; height: 52px; }
  .envelope-back.white { top: 186px; height: 66px; }
</style>
</head>
<body>

<section class="identity-panel">
  <div class="brand-lockup">
    <div class="mark"></div>
    <div class="name">The Guiding Spark LLC</div>
    <div class="tagline">because everyone deserves a fan</div>
  </div>

  <div class="card card-back">
    <div class="title">Our Time Together</div>
    <div class="field">Date:</div>
    <div class="field">Time:</div>
    <div>Ask about our Friend Bonus program</div>
  </div>

  <div class="card card-front">
    <div class="mini-brand"><div class="dot"></div><span>The Guiding Spark LLC</span></div>
    <div class="person">Rosalind K Delgado</div>
    <div>Personal Mentor</div>
    <svg class="wave" viewBox="0 0 80 14" preserveAspectRatio="none">
      <path d="M0 8 Q40 0 80 6 L80 14 L0 14Z" fill="var(--orange)"/>
      <path d="M0 10 Q40 3 80 9 L80 14 L0 14Z" fill="var(--blue)"/>
    </svg>
  </div>

  <div class="card card-contact">
    <div class="person">Rosalind K Delgado</div>
    <div>Personal Mentor</div>
    <div style="margin-top:3px">2871 S Whitcomb Ave Garden Unit<br>Chicago IL 60619</div>
    <div>rdelgado@theguidingspark.example</div>
    <div>www.theguidingspark.example</div>
  </div>

  <div class="card card-promo">
    <div class="dot"></div>
    <span>The Guiding Spark LLC</span>
  </div>
</section>

<article class="letterhead first">
  <div class="mini-brand"><div class="dot"></div><span>The Guiding Spark LLC</span></div>
  <div class="address">2871 S Whitcomb Ave Garden Unit Chicago IL 60619<br>rdelgado@theguidingspark.example</div>
  <div class="backdrop-mark"></div>
  <div class="backdrop-name">The Guiding Spark LLC</div>
  <svg class="wave" viewBox="0 0 136 26" preserveAspectRatio="none">
    <path d="M0 12 Q70 -2 136 10 L136 26 L0 26Z" fill="var(--orange)"/>
    <path d="M0 16 Q70 4 136 14 L136 26 L0 26Z" fill="var(--blue)"/>
  </svg>
  <div class="footer-web">www.theguidingspark.example</div>
</article>

<article class="letterhead second">
  <div class="mini-brand"><div class="dot"></div><span>The Guiding Spark LLC</span></div>
  <div class="address">2871 S Whitcomb Ave Garden Unit Chicago IL 60619<br>rdelgado@theguidingspark.example</div>
  <div class="backdrop-mark"></div>
  <div class="backdrop-name">The Guiding Spark LLC</div>
  <svg class="wave" viewBox="0 0 136 26" preserveAspectRatio="none">
    <path d="M0 12 Q70 -2 136 10 L136 26 L0 26Z" fill="var(--orange)"/>
    <path d="M0 16 Q70 4 136 14 L136 26 L0 26Z" fill="var(--blue)"/>
  </svg>
  <div class="footer-web">www.theguidingspark.example</div>
</article>

<article class="envelope-front">
  <div class="mini-brand"><div class="dot"></div><span>The Guiding Spark LLC</span></div>
  <div class="return">2871 S Whitcomb Ave Garden Unit Chicago IL 60619</div>
  <svg class="wave" viewBox="0 0 110 18" preserveAspectRatio="none">
    <path d="M0 8 Q55 -2 110 7 L110 18 L0 18Z" fill="var(--orange)"/>
    <path d="M0 11 Q55 2 110 10 L110 18 L0 18Z" fill="var(--blue)"/>
  </svg>
</article>

<div class="envelope-back green">
  <svg viewBox="0 0 161 52" preserveAspectRatio="none">
    <defs><linearGradient id="gFlap" x1="0" y1="0" x2="0" y2="1"><stop offset="0" stop-color="#a9db6c"/><stop offset="1" stop-color="#3e9a3a"/></linearGradient></defs>
    <rect width="161" height="52" fill="#f7f8f9"/>
    <path d="M0 0 H161 V22 L80.5 42 L0 22Z" fill="url(#gFlap)"/>
    <circle cx="80.5" cy="24" r="6" fill="#fff"/>
  </svg>
</div>
<div class="envelope-back blue">
  <svg viewBox="0 0 161 52" preserveAspectRatio="none">
    <defs><linearGradient id="bFlap" x1="0" y1="0" x2="0" y2="1"><stop offset="0" stop-color="#3d8fd8"/><stop offset="1" stop-color="#0f3c74"/></linearGradient></defs>
    <rect width="161" height="52" fill="#f7f8f9"/>
    <path d="M0 0 H161 V22 L80.5 42 L0 22Z" fill="url(#bFlap)"/>
    <circle cx="80.5" cy="24" r="6" fill="#fff"/>
  </svg>
</div>
<div class="envelope-back white">
  <svg viewBox="0 0 161 66" preserveAspectRatio="none">
    <rect width="161" height="66" fill="#fff"/>
    <path d="M0 0 L80.5 34 L161 0" fill="none" stroke="#d4d9df" stroke-width="1"/>
    <path d="M0 66 L70 30 M161 66 L91 30" fill="none" stroke="#e6e9ed" stroke-width="1"/>
    <circle cx="80.5" cy="30" r="6" fill="var(--blue-light)"/>
  </svg>
</div>

</body>
</html>
```